Investment Funding, Building and Construction

I need a design logo for my new business based out of Houston, TX called Kestrel Ridge Holdings LLC., We are a company looking to help fund and invest into other small/businesses that do not want to deal with the banking system. We also remodel, renovate, and build from the ground up anything from residential, industrial warehousing, and commercial buildings. We would like the design to express our great deal of passion that we have for the work, our dedication to helping the costumer/businesses receive their expectation of work and also our professionalism and commitment to making sure we get the job done as perfect as possible. We want to build your future!

Target Market(s)

Architects, Design Companies, Home Owners and Real Estate

Industry/Entity Type

Construction Company

Contact Information for Business Card

Name: Dorian Welsby
Position: CEO/President
Company Name: Kestrel Ridge Holdings LLC.,
Website: www.kestrelridgeholds.example
Phone: 281-555-0173
Email: kestrelridgeholds@mailbox.example, crewfundline@mailbox.example

Font styles to use
Serif

Colors
f04a50
3377b5

Requirements
Must have
• Motivational, Inspiring, and Detailed oriented work but simple.
Nice to have
• I would like to see excitement and enthusiasm within the card.
Should not have
• The project can not be boring and lack of detail.

```html
<!DOCTYPE html>
<html lang="en">
<head>
<meta charset="utf-8">
<title>Kestrel Ridge Holdings LLC – Business Card</title>
<link href="https://fonts.googleapis.com/css2?family=Roboto+Slab:wght@600;700&family=Source+Serif+4:wght@400;600&display=swap" rel="stylesheet">
<style>
  :root {
    --backdrop: #9a9a9a;
    --card-white: #ffffff;
    --brand-blue: #3377b5;
    --brand-red: #f04a50;
    --ink-dark: #3f3f3f;
    --ink-body: #2b2b2b;
    --rule-grey: #d9d9d9;
  }
  * { box-sizing: border-box; margin: 0; padding: 0; }
  html, body { width: 1200px; height: 900px; overflow: hidden; }
  body { background: var(--backdrop); position: relative; font-family: "Source Serif 4", Georgia, serif; }

  .card { position: absolute; box-shadow: 2px 3px 5px rgba(0,0,0,0.35); }
  .card--front {
    left: 120px; top: 275px; width: 478px; height: 295px;
    background: var(--card-white);
    border-radius: 0 52px 0 52px;
  }
  .card--back {
    left: 607px; top: 274px; width: 476px; height: 293px;
    background: var(--brand-blue);
    border-radius: 52px 0 52px 0;
  }

  .wordmark {
    position: absolute;
    display: flex; align-items: center; gap: 12px;
    font-family: "Roboto Slab", Georgia, serif;
    font-weight: 700;
    text-transform: uppercase;
    line-height: 1.1;
  }
  .wordmark__square { width: 18px; height: 18px; flex: none; background: var(--brand-red); }
  .wordmark__name { font-size: 27px; letter-spacing: 0.2px; }

  .card--front .wordmark { right: 35px; top: 44px; text-align: right; color: var(--ink-dark); }
  .card--back .wordmark { left: 102px; top: 100px; color: var(--card-white); }

  .holder { position: absolute; left: 30px; top: 160px; right: 35px; }
  .holder__name {
    font-family: "Roboto Slab", Georgia, serif; font-weight: 700;
    font-size: 17px; color: var(--brand-blue); letter-spacing: 0.3px;
  }
  .holder__role-row { display: flex; align-items: center; gap: 6px; margin-top: 1px; }
  .holder__role { font-size: 12.5px; color: var(--ink-body); white-space: nowrap; }
  .holder__rule { flex: 1; height: 1px; background: var(--rule-grey); }

  .contact-list { position: absolute; left: 30px; top: 202px; list-style: none; }
  .contact-list li {
    display: flex; align-items: center; gap: 3px;
    font-size: 12px; color: var(--ink-body); height: 17.5px; white-space: nowrap;
  }
  .contact-list svg { width: 11px; height: 11px; fill: var(--brand-red); flex: none; }

  .address {
    position: absolute; right: 34px; top: 234px; font-style: normal;
    text-align: right; font-size: 12px; line-height: 17.5px; color: var(--ink-body);
  }
</style>
</head>
<body>
  <section class="card card--front">
    <div class="wordmark">
      <span class="wordmark__square"></span>
      <span class="wordmark__name">Kestrel Ridge<br>Holdings LLC</span>
    </div>

    <div class="holder">
      <h1 class="holder__name">DORIAN WELSBY</h1>
      <div class="holder__role-row">
        <span class="holder__role">CEO/President</span>
        <span class="holder__rule"></span>
      </div>
    </div>

    <ul class="contact-list">
      <li>
        <svg viewBox="0 0 12 12" aria-hidden="true"><path d="M1 4c0-2 2-3 5-3s5 1 5 3l-2 1-1-1.5H4L3 5zM2.5 6h7l1 5h-9z"/></svg>
        281-555-0173
      </li>
      <li>
        <svg viewBox="0 0 12 12" aria-hidden="true"><path d="M3.5 0h5a1 1 0 0 1 1 1v10a1 1 0 0 1-1 1h-5a1 1 0 0 1-1-1V1a1 1 0 0 1 1-1zm.5 1.5v7.5h4V1.5zM6 10a.6.6 0 1 0 0 1.2A.6.6 0 0 0 6 10z"/></svg>
        281-555-0173
      </li>
      <li>
        <svg viewBox="0 0 12 12" aria-hidden="true"><path d="M0 2.5h12v7H0zm1 .7v.3l5 3 5-3v-.3z"/></svg>
        kestrelridgeholds@mailbox.example
      </li>
      <li>
        <svg viewBox="0 0 12 12" aria-hidden="true"><circle cx="6" cy="6" r="5.5"/><path d="M3 4l2 1 0 2 2 1 1 2" stroke="#fff" stroke-width="1" fill="none"/></svg>
        www.kestrelridgeholds.example
      </li>
    </ul>

    <address class="address">
      12345, Address Goes Here<br>
      Country Name, 123456
    </address>
  </section>

  <section class="card card--back">
    <div class="wordmark">
      <span class="wordmark__square"></span>
      <span class="wordmark__name">Kestrel Ridge<br>Holdings LLC</span>
    </div>
  </section>
</body>
</html>
```